Rug Cleaning Web Design Project

We need a web design for our cleaning company. We currently have a web page but are not happy with its design. We currently offer fine rug cleaning,upholstery cleaning, and residential and commercial carpet cleanning. We also offer water damage restoration. For our rug cleaning services we offer : Enzyme treatments for pet contamination and odor removal, application of stain protection that is designed for the fine textiles used in rug construction, application of treatments designed to prevent moth damage and pads designed to be used under rugs.Our current web site is harborfreshcare.example. We are intrested in a design with similar information to the web page of Velmora Rug Cleaners INC. We would like to use the colors that are present in our logo that will be uploaded with this description. We would also like this new page to be linked to our other address loomrinsepro.example. We would like the deign to be visually attractive but not "too busy".
Updates

Please include pictures of rugs, or people washing rugs if possible. We do not offer maid type cleaning services. We would not be interested in designs including pictures depicting that type service. Thanks for your hard work on this project.

Dana Whitlow

Industry/Entity Type

Residential

Requirements
Must have
• This page must be viewable on smart phones and tablets.

```html
<!DOCTYPE html>
<html lang="en">
<head>
<meta charset="utf-8">
<title>Loom Rinse Pro</title>
<meta name="viewport" content="width=1200">
<link href="https://fonts.googleapis.com/css2?family=Roboto+Slab:wght@300;400&family=Open+Sans:ital,wght@0,400;1,700&family=Josefin+Sans:wght@300;400&display=swap" rel="stylesheet">
<style>
:root{
  --bg-top:#676767;
  --bg-bottom:#ffffff;
  --panel:#ffffff;
  --blue:#1e73b9;
  --blue-dark:#0b3d7a;
  --blue-light:#3aa0de;
  --navy-tab:#0a2f6b;
  --orange:#f2661c;
  --ink:#4a4a4a;
  --ink-dark:#222;
  --slider-dark:#2a2a2a;
  --footer-top:#cfcfcf;
  --footer-bottom:#f3f3f3;
  --footer-ink:#333;
  --link:#2a3f8f;
}
*{margin:0;padding:0;box-sizing:border-box}
html,body{width:1200px;height:1115px;overflow:hidden}
body{
  position:relative;
  background:linear-gradient(to bottom,var(--bg-top) 0,#9a9a9a 300px,#e8e8e8 560px,var(--bg-bottom) 640px);
  font-family:"Roboto Slab",Georgia,serif;
  color:var(--ink);
}
.page-top{position:absolute;left:0;top:0;width:1200px;height:200px}
.page-body{position:absolute;left:139px;top:110px;width:923px;height:842px;background:var(--panel);box-shadow:0 0 14px rgba(0,0,0,.18)}
.brand{position:absolute;left:168px;top:104px;display:flex;align-items:center;gap:12px}
.brand-dot{width:50px;height:50px;border-radius:50%;background:var(--blue)}
.brand-name{font-family:"Roboto Slab",Georgia,serif;font-weight:400;font-size:31px;color:var(--ink-dark);letter-spacing:-.5px;white-space:nowrap}
.rug-strip{position:absolute;left:480px;top:108px;width:326px;height:78px;background:linear-gradient(100deg,#c9452a,#e07a3a 45%,#b53a2a 70%,#d96a32);border-radius:2px}
.contact-top{position:absolute;right:178px;top:106px;text-align:right}
.phone{font-family:"Open Sans",Arial,sans-serif;font-style:italic;font-weight:700;font-size:26px;color:#111;letter-spacing:.5px}
.phone .area{color:var(--orange)}
.email-top{font-family:"Open Sans",Arial,sans-serif;font-size:13px;color:#222;margin-top:2px}
.main-nav{position:absolute;left:168px;top:186px;width:864px;height:41px;background:linear-gradient(to bottom,#2a8ad6,#1668b3 82%,var(--navy-tab) 82%)}
.main-nav ul{list-style:none;display:flex;height:34px}
.main-nav li{font-size:14px;color:#fff;text-transform:uppercase;line-height:34px;white-space:nowrap}
.main-nav li.active{background:var(--navy-tab)}
.main-nav li:nth-child(1){margin-left:24px;width:83px;text-align:center}
.main-nav li:nth-child(2){margin-left:27px}
.main-nav li:nth-child(3){margin-left:48px}
.main-nav li:nth-child(4){margin-left:49px}
.main-nav li:nth-child(5){margin-left:49px}
.main-nav li:nth-child(6){margin-left:50px}
.hero{position:absolute;left:168px;top:227px;width:864px;height:324px;overflow:hidden;background:var(--slider-dark)}
.hero-photo{position:absolute;top:0;height:324px}
.photo-plumber{left:0;width:278px;background:linear-gradient(135deg,#e9eef3,#b9cbe0 60%,#8aa7c8)}
.photo-family{left:278px;width:326px;background:linear-gradient(160deg,#f2ece4,#e3d2bf 55%,#f4f2ee)}
.photo-vacuum{left:604px;width:260px;background:linear-gradient(180deg,#e8ecef,#c9d5dc 55%,#b9a88d)}
.hero-shape{position:absolute;left:0;top:0}
.hero-arrows{position:absolute;left:188px;top:463px;display:flex;gap:6px}
.hero-title{position:absolute;left:188px;top:504px;font-family:"Josefin Sans",Arial,sans-serif;color:#fff;font-size:33px;font-weight:400;white-space:nowrap}
.hero-title small{font-size:19px;font-weight:300;color:var(--blue-light);margin-left:2px}
.welcome-photo{position:absolute;left:154px;top:578px;width:206px;height:298px;background:linear-gradient(to bottom,#f4f4f4,#2fa25b 25%,#2c3f5c 60%,#e9e9e9);border-radius:4px}
.welcome{position:absolute;left:390px;top:590px;width:650px}
.welcome h1{font-weight:400;font-size:27px;color:var(--blue);letter-spacing:.3px;margin-bottom:20px;white-space:nowrap}
.welcome p{font-weight:300;font-size:17.5px;line-height:24px;color:var(--ink);margin-bottom:24px}
.welcome .award{color:var(--orange)}
.site-footer{position:absolute;left:0;top:950px;width:1200px;height:165px;background:linear-gradient(to bottom,var(--footer-top),var(--footer-bottom) 60%);border-top:1px solid #bdbdbd}
.footer-col{position:absolute;top:28px}
.footer-icon{position:absolute;width:48px;height:48px;top:30px}
.footer-col h2{font-weight:400;font-size:20px;color:var(--blue-dark);margin-bottom:6px}
.footer-col p{font-size:14px;line-height:21px;color:var(--footer-ink);white-space:nowrap}
.footer-col .link{color:var(--link)}
.footer-col .note{font-size:11px;margin-top:2px}
.col-support{left:234px}
.col-contact{left:541px}
.award-badge{position:absolute;left:834px;top:984px;width:132px;height:78px;border-radius:6px;background:#f7f7f7;box-shadow:0 0 0 2px #e2e2e2 inset}
.copyright{position:absolute;left:835px;top:1073px;font-size:12.5px;color:var(--footer-ink);white-space:nowrap}
</style>
</head>
<body>
<svg class="page-top" width="1200" height="200" viewBox="0 0 1200 200" aria-hidden="true">
  <path d="M139 76 Q560 14 1062 84 L1062 200 L139 200 Z" fill="#ffffff"/>
  <path d="M470 36 Q820 26 1045 70 L1062 84 Q800 40 470 38 Z" fill="#3a93d2"/>
</svg>
<div class="page-body"></div>

<header>
  <div class="brand"><span class="brand-dot"></span><span class="brand-name">Loom Rinse Pro</span></div>
  <div class="rug-strip" role="img" aria-label="Three patterned oriental rugs laid side by side"></div>
  <div class="contact-top">
    <div class="phone"><span class="area">(555)</span> 014-2290</div>
    <div class="email-top">care@harborfreshcare.example</div>
  </div>
  <nav class="main-nav">
    <ul>
      <li class="active">Home</li>
      <li>About Us</li>
      <li>Rug Washing</li>
      <li>Water Damage</li>
      <li>Carpet Cleaning</li>
      <li>Contact Us</li>
    </ul>
  </nav>
</header>

<section class="hero">
  <div class="hero-photo photo-plumber" role="img" aria-label="Smiling technician in cap working on water pipes"></div>
  <div class="hero-photo photo-family" role="img" aria-label="Happy family lying on a soft white carpet"></div>
  <div class="hero-photo photo-vacuum" role="img" aria-label="Technician cleaning office carpet with a wand"></div>
  <svg class="hero-shape" width="864" height="324" viewBox="0 0 864 324" aria-hidden="true">
    <path d="M0 180 L604 268 Q740 280 864 286 L864 324 L0 324 Z" fill="#2a2a2a"/>
    <path d="M604 268 Q740 280 864 286" stroke="#f2661c" stroke-width="3" fill="none"/>
    <path d="M604 272 Q740 284 864 292" stroke="#3aa0de" stroke-width="1.5" fill="none"/>
  </svg>
</section>
<div class="hero-arrows" aria-hidden="true">
  <svg width="23" height="23" viewBox="0 0 23 23"><circle cx="11.5" cy="11.5" r="10" fill="#777" stroke="#ccc" stroke-width="1.5"/><path d="M13 7 L8.5 11.5 L13 16 M8.5 11.5 H16" stroke="#eee" stroke-width="1.8" fill="none"/></svg>
  <svg width="23" height="23" viewBox="0 0 23 23"><circle cx="11.5" cy="11.5" r="10" fill="#777" stroke="#ccc" stroke-width="1.5"/><path d="M10 7 L14.5 11.5 L10 16 M14.5 11.5 H7" stroke="#eee" stroke-width="1.8" fill="none"/></svg>
</div>
<h2 class="hero-title">Need Some Help? <small>Call us for Confidential Advice &amp; Support</small></h2>

<main>
  <div class="welcome-photo" role="img" aria-label="Cleaning technician in green sweater standing with a canister vacuum"></div>
  <section class="welcome">
    <h1>WELCOME TO LOOM RINSE PRO</h1>
    <p>When it comes to cleaning carpet, oriental rugs, area rugs or furniture ~ any fabric from antique silk brocades to contemporary carpet fibers ~ our service is unparalled.</p>
    <p>Harborfresh Care &amp; Restoration is the recipient of the 2018 &amp; 2019 <span class="award">"BEST IN BUSINESS AWARD"</span> in Brookvale County for Water Damage Restoration and Carpet and Rug Cleaning.</p>
    <p>Please contact us for an extensive list of references.</p>
  </section>
</main>

<footer class="site-footer">
  <svg class="footer-icon" style="left:168px" viewBox="0 0 48 48" aria-hidden="true">
    <circle cx="24" cy="24" r="22" fill="none" stroke="#1e73b9" stroke-width="3"/>
    <path d="M12 16 h16 a3 3 0 0 1 3 3 v7 a3 3 0 0 1 -3 3 h-9 l-5 4 v-4 h-2 a3 3 0 0 1 -3 -3 v-7 a3 3 0 0 1 3 -3z" fill="#1e73b9"/>
    <path d="M33 21 h3 a3 3 0 0 1 3 3 v6 a3 3 0 0 1 -3 3 v4 l-5 -4 h-7" fill="none" stroke="#1e73b9" stroke-width="2.5"/>
  </svg>
  <div class="footer-col col-support">
    <h2>SUPPORT</h2>
    <p>Please contact for support</p>
    <p class="link">(555) 014-2290</p>
    <p class="link">care@harborfreshcare.example</p>
  </div>
  <svg class="footer-icon" style="left:476px" viewBox="0 0 48 48" aria-hidden="true">
    <circle cx="24" cy="24" r="22" fill="none" stroke="#1e73b9" stroke-width="3"/>
    <circle cx="24" cy="18" r="6" fill="#1e73b9"/>
    <path d="M13 34 a11 9 0 0 1 22 0 z" fill="#1e73b9"/>
  </svg>
  <div class="footer-col col-contact">
    <h2>CONTACT US</h2>
    <p>Harborfresh Care &amp; Restoration</p>
    <p>48 Alder Lane</p>
    <p>Brookvale, OR&nbsp; 97000</p>
    <p class="note">Serving Brookvale &amp; surrounding areas.</p>
  </div>
</footer>
<div class="award-badge" aria-hidden="true"></div>
<p class="copyright">Copyright © 2012 Loom Rinse Pro.</p>
</body>
</html>
```